Prime Care Company - Inside Back Cover of KESTO Magazine Ad -

We need a full page ad that can also be expanded into a full two page - For Prime Care Residential Services Company - QNV Cleaning is the Largest in the country (UAE) Hurra Mendo, (Maintenance, Pest Control, AC Duct Cleaning and Remodeling)

Please see all logos attached
There are two pervious fliers for EXAMPLE ONLY - do NOT want something that looks the same - want new & fresh!

Target Market(s)

Families, Airport Lounges, Hotels and Airline travelers will all view this Magazine.

Industry/Entity Type

Residential

Font styles to use
Serif

Colors

Designer to choose colors to be used in the design.

Requirements
Must have
• Sizes
• Double Page Spread Advert
• (DPS) 265mm (h) x 448mm (w)
• Full Page Specs:
• Ø Trim W200 x H265 mm
• Ø Bleed W210 x H275 mm
• Ø Type W195 x H250 mm
• Bleed
• Artwork for all adverts must include a 5mm bleed on all sides (see sizes above), all text and images should be at least a further 5mm from the crop guides. The easiest way of thinking of this if you are uncertain is to ensure the
• background image goes to right to the edge of the file and then all text, logos, etc are at least 8mm from the edges. To ensure correct printing an appropriate border will be added to all artwork supplied without correct bleeds.
• Colour
• Artwork should be completed and saved in CMYK process, Please delete all unused colour swatches from the colour palettes. Do not use Pantone or similar colours
Nice to have
• Clean - easy to read -
• Bright Colors
• Should be different

```html
<!DOCTYPE html>
<html lang="en">
<head>
<meta charset="utf-8">
<title>Pest Control Service – Advert</title>
<link href="https://fonts.googleapis.com/css2?family=Montserrat:wght@400;500;600;700;800&family=Oswald:wght@500;600&display=swap" rel="stylesheet">
<style>
  :root {
    --backdrop: #2a2a2b;
    --orange: #f7941d;
    --orange-light: #f9a23a;
    --navy: #233e92;
    --navy-deep: #1d3585;
    --white: #ffffff;
    --paper-grey: #efefef;
    --ring-grey: #e6e6e8;
    --red: #b8202a;
    --text-navy: #243c8f;
    --text-grey: #555a66;
  }
  html, body {
    margin: 0;
    padding: 0;
    width: 962px;
    height: 1200px;
    overflow: hidden;
    background: var(--backdrop);
  }
  .canvas {
    position: relative;
    width: 962px;
    height: 1200px;
  }
  .advert {
    position: absolute;
    left: 31px;
    top: 334px;
    width: 1096px;
    height: 648px;
    transform: scale(0.8212);
    transform-origin: top left;
    background: var(--white);
    overflow: hidden;
    font-family: "Montserrat", Arial, sans-serif;
  }
  .header {
    position: absolute;
    left: 0; top: 0;
    width: 1096px; height: 151px;
    background: linear-gradient(90deg, var(--orange) 0%, var(--orange-light) 60%, var(--orange) 100%);
  }
  .header__title {
    position: absolute;
    left: 50px; top: 34px;
    margin: 0;
    color: var(--white);
    font-weight: 700;
    font-size: 76px;
    letter-spacing: -0.5px;
    line-height: 1;
    white-space: nowrap;
  }
  .header__tagline {
    position: absolute;
    left: 899px; top: 44px;
    margin: 0;
    color: var(--white);
    font-family: "Oswald", Arial, sans-serif;
    font-weight: 500;
    font-size: 24px;
    line-height: 27px;
    text-transform: uppercase;
  }
  .header__rule {
    position: absolute;
    left: 900px; top: 104px;
    width: 196px; height: 7px;
    background: var(--navy);
  }
  .team-photo {
    position: absolute;
    left: 0; top: 151px;
    width: 1096px; height: 297px;
    background:
      linear-gradient(180deg, rgba(236,236,238,0.9) 0%, rgba(200,205,215,0.4) 22%, rgba(0,0,0,0) 40%),
      linear-gradient(90deg, #6a6f7c 0%, #5c6478 35%, #8f7f95 65%, #c79aae 85%, #b9a895 100%);
  }
  .services-band {
    position: absolute;
    left: 0; top: 448px;
    width: 930px; height: 28px;
    background: var(--navy);
    color: var(--white);
    font-weight: 700;
    font-size: 17px;
    line-height: 28px;
  }
  .services-band__label {
    position: absolute;
    left: 50px; top: 0;
    display: flex; align-items: center; gap: 9px;
  }
  .services {
    position: absolute;
    left: 48px; top: 503px;
    margin: 0; padding: 0;
    list-style: none;
    color: var(--text-navy);
    font-weight: 500;
    font-size: 18px;
    line-height: 27px;
    text-transform: uppercase;
  }
  .services--second { left: 345px; line-height: 21px; top: 505px; }
  .services li {
    display: flex;
    align-items: flex-start;
    gap: 4px;
  }
  .services li svg { flex: none; margin-top: 6px; }
  .services--second li svg { margin-top: 3px; }
  .services--second li + li { margin-top: 11px; }
  .footer-strip {
    position: absolute;
    left: 0; top: 593px;
    width: 1096px; height: 55px;
    background: var(--paper-grey);
  }
  .brand-names {
    position: absolute;
    left: 630px; top: 506px;
    display: flex; gap: 20px;
    align-items: center;
  }
  .brand-name {
    display: flex; align-items: center; gap: 6px;
    color: var(--text-navy);
    font-weight: 700;
    font-size: 12px;
    white-space: nowrap;
  }
  .brand-name__dot {
    width: 10px; height: 10px;
    border-radius: 50%;
    background: var(--orange);
  }
  .credentials {
    position: absolute;
    left: 639px; top: 549px;
    margin: 0; padding: 0;
    list-style: none;
    color: var(--text-grey);
    font-size: 10.5px;
    line-height: 13px;
    text-transform: uppercase;
  }
  .credentials li { display: flex; align-items: center; gap: 3px; }
  .call-to-action {
    position: absolute;
    left: 639px; top: 596px;
    width: 302px; height: 30px;
    background: var(--orange);
    color: var(--white);
    font-size: 15px;
    line-height: 30px;
    text-align: center;
    text-transform: uppercase;
  }
  .call-to-action strong { font-weight: 700; }
  .phone-box {
    position: absolute;
    left: 946px; top: 596px;
    width: 119px; height: 30px;
    background: var(--red);
    color: var(--white);
    font-family: "Oswald", Arial, sans-serif;
    font-weight: 600;
    font-size: 20px;
    line-height: 30px;
    text-align: center;
  }
  .discount-badge {
    position: absolute;
    left: 913px; top: 414px;
    width: 160px; height: 160px;
    border-radius: 50%;
    background: var(--ring-grey);
    box-shadow: 0 3px 8px rgba(0,0,0,0.18);
  }
  .discount-badge__core {
    position: absolute;
    left: 12px; top: 12px;
    width: 136px; height: 136px;
    border-radius: 50%;
    background: var(--navy-deep);
    color: var(--white);
    text-align: center;
    text-transform: uppercase;
  }
  .discount-badge__value {
    display: block;
    margin-top: 24px;
    font-weight: 800;
    font-size: 44px;
    line-height: 1;
  }
  .discount-badge__value sup { font-size: 24px; vertical-align: 14px; }
  .discount-badge__note {
    display: block;
    margin-top: 6px;
    font-weight: 700;
    font-size: 13px;
    line-height: 15px;
  }
</style>
</head>
<body>
<div class="canvas">
  <article class="advert">
    <header class="header">
      <h1 class="header__title">Pest Control Service</h1>
      <p class="header__tagline">Your Property,<br>Our Priorety</p>
      <div class="header__rule"></div>
    </header>

    <div class="team-photo" role="img" aria-label="Group photo of the full company team in uniform standing in front of a long row of branded service vans"></div>

    <div class="services-band">
      <div class="services-band__label">
        <svg width="17" height="17" viewBox="0 0 17 17" aria-hidden="true"><circle cx="8.5" cy="8.5" r="8.5" fill="#f7941d"/><path d="M5 6.5 L8.5 10 L12 6.5" fill="none" stroke="#fff" stroke-width="2.2" stroke-linecap="round" stroke-linejoin="round"/></svg>
        <span>OUR SERVICES</span>
      </div>
    </div>

    <ul class="services">
      <li><svg width="14" height="14" viewBox="0 0 14 14" aria-hidden="true"><circle cx="7" cy="7" r="7" fill="#f7941d"/><path d="M5.5 4 L8.5 7 L5.5 10" fill="none" stroke="#fff" stroke-width="2" stroke-linecap="round" stroke-linejoin="round"/></svg>General Pest Control</li>
      <li><svg width="14" height="14" viewBox="0 0 14 14" aria-hidden="true"><circle cx="7" cy="7" r="7" fill="#f7941d"/><path d="M5.5 4 L8.5 7 L5.5 10" fill="none" stroke="#fff" stroke-width="2" stroke-linecap="round" stroke-linejoin="round"/></svg>Bed Bug Control</li>
      <li><svg width="14" height="14" viewBox="0 0 14 14" aria-hidden="true"><circle cx="7" cy="7" r="7" fill="#f7941d"/><path d="M5.5 4 L8.5 7 L5.5 10" fill="none" stroke="#fff" stroke-width="2" stroke-linecap="round" stroke-linejoin="round"/></svg>Rat Control</li>
    </ul>
    <ul class="services services--second">
      <li><svg width="14" height="14" viewBox="0 0 14 14" aria-hidden="true"><circle cx="7" cy="7" r="7" fill="#f7941d"/><path d="M5.5 4 L8.5 7 L5.5 10" fill="none" stroke="#fff" stroke-width="2" stroke-linecap="round" stroke-linejoin="round"/></svg><span>Cockroaches<br>Control</span></li>
      <li><svg width="14" height="14" viewBox="0 0 14 14" aria-hidden="true"><circle cx="7" cy="7" r="7" fill="#f7941d"/><path d="M5.5 4 L8.5 7 L5.5 10" fill="none" stroke="#fff" stroke-width="2" stroke-linecap="round" stroke-linejoin="round"/></svg>Ant Control</li>
    </ul>

    <div class="footer-strip"></div>

    <div class="brand-names">
      <span class="brand-name"><span class="brand-name__dot"></span>QNV Pest Control</span>
      <span class="brand-name"><span class="brand-name__dot"></span>QNV Cleaning</span>
    </div>

    <ul class="credentials">
      <li><svg width="8" height="8" viewBox="0 0 8 8" aria-hidden="true"><circle cx="4" cy="4" r="4" fill="#f7941d"/></svg>European Managed</li>
      <li><svg width="8" height="8" viewBox="0 0 8 8" aria-hidden="true"><circle cx="4" cy="4" r="4" fill="#f7941d"/></svg>Residential/ Comercial/ Maintenance Contracts</li>
      <li><svg width="8" height="8" viewBox="0 0 8 8" aria-hidden="true"><circle cx="4" cy="4" r="4" fill="#f7941d"/></svg>On Call Services</li>
    </ul>

    <div class="call-to-action"><strong>Call us</strong> now for a free estimate!</div>
    <div class="phone-box">800 SHIELDS</div>

    <div class="discount-badge">
      <div class="discount-badge__core">
        <span class="discount-badge__value">10<sup>%</sup></span>
        <span class="discount-badge__note">For our<br>QNV Clients</span>
      </div>
    </div>
  </article>
</div>
</body>
</html>
```